Business card for Chiropractic clinics needs reworked / redesigned

The business card in attachment was designed 10 years ago. It is in need of an update.
We have 2 clinics:
VELDHOVE KLINIEK & VELDHOVE KLINIEK NOORD
Only one address needs to be on the card for doctors that only work in one clinic and two addresses need to be on the card for the doctors that work in both clinics.

Target Market(s)

patients/referrers

Industry/Entity Type

Medical

Contact Information for Business Card

Logo (in full or zoomed-in)
Clinic Name
Doctor name and title
clinic address, website, tel, email

Font styles to use
Sans Serif

Colors

Designer to choose colors to be used in the design.

Requirements
Must have
• Good contrast/readability
• We like modern minimalistic designs
• The Bcard needs to project our very high standard of proficiency/professionalism
Should not have
• Not curly
• Not to much colours

```html
<!DOCTYPE html>
<html lang="nl">
<head>
<meta charset="utf-8">
<title>Veldhove Kliniek – Visitekaartje</title>
<link rel="stylesheet" href="https://fonts.googleapis.com/css2?family=Inter:ital,wght@0,300;0,400;1,300&display=swap">
<style>
  :root {
    --green-dark: #667e1d;
    --green-light: #a3d46f;
    --text-grey: #444444;
    --white: #ffffff;
  }
  * { margin: 0; padding: 0; box-sizing: border-box; }
  html, body { width: 1200px; height: 389px; overflow: hidden; background: var(--white); }
  body { font-family: "Inter", Helvetica, Arial, sans-serif; }

  .card { position: relative; width: 1200px; height: 389px; display: flex; }

  .card-front { position: relative; width: 600px; height: 389px; background: var(--white); }
  .card-back  { position: relative; width: 600px; height: 389px; background: var(--green-light); }

  .doctor { position: absolute; left: 0; width: 600px; top: 82px; text-align: center; }
  .doctor-name {
    font-size: 24px; font-weight: 400; letter-spacing: 2.4px;
    color: var(--green-dark); line-height: 1;
  }
  .doctor-title {
    margin-top: 9px; font-size: 18px; font-weight: 300; font-style: italic;
    color: var(--text-grey); line-height: 1;
  }

  .clinic { position: absolute; top: 264px; font-size: 16px; color: var(--text-grey); line-height: 20px; }
  .clinic-main  { left: 42px; text-align: left; }
  .clinic-north { right: 42px; text-align: right; }
  .clinic-name { font-size: 17px; margin-bottom: 7px; }
  .clinic-name .accent { color: var(--green-dark); }
  .label { color: var(--green-dark); }

  .brand { position: absolute; left: 0; width: 600px; top: 188px; text-align: center; }
  .brand-name {
    font-size: 36px; font-weight: 300; letter-spacing: 6px;
    color: var(--green-dark); line-height: 1; padding-left: 6px;
  }
  .brand-rule { width: 268px; height: 1px; background: var(--green-dark); margin: 12px auto 0; }
  .locations { margin-top: 28px; font-size: 20px; font-weight: 300; color: var(--white); letter-spacing: 1px; line-height: 30px; }
</style>
</head>
<body>
<div class="card">
  <section class="card-front">
    <div class="doctor">
      <p class="doctor-name">LUKAS VERHAEGHE</p>
      <p class="doctor-title">Chiropractor</p>
    </div>
    <div class="clinic clinic-main">
      <p class="clinic-name">VELDHOVE <span class="accent">KLINIEK</span></p>
      <p>Kouterlaan 148</p>
      <p><span class="label">t:</span> +32 (0) 9 555.01.24</p>
      <p>www.veldhovekliniek.be</p>
    </div>
    <div class="clinic clinic-north">
      <p class="clinic-name">VELDHOVE KLINIEK <span class="accent">NOORD</span></p>
      <p>Molenstraat 41</p>
      <p><span class="label">t:</span> +32 (0) 9 555.07.86</p>
      <p>www.veldhovenoord.be</p>
    </div>
  </section>
  <section class="card-back">
    <div class="brand">
      <p class="brand-name">VELDHOVE</p>
      <div class="brand-rule"></div>
      <div class="locations">
        <p>KLINIEK</p>
        <p>NOORD</p>
      </div>
    </div>
  </section>
</div>
</body>
</html>
```